New business card design needed for Diesel Fitting (Mechanical) Company

We need a new business card for our company called "Gumtree Engine Works" that showcases our logo and business details.
Target Market(s)
Owners of all makes and models of vehicles, trucks, plant and machinery.
Industry/Entity Type
Mechanical
Contact Information for Business Card
The business card details need to include the following: Owners/Directors: Doug & Marisol Brent-Coyle ABN: 41 917 302 846 Address: 317 Wattlebrook Street BINDARRA CREEK QLD 4873 Postal Address: PO Box 5791 BINDARRA CREEK QLD 4873 Website: www.gewservice.com.au Phone: 4712 9083 Mobile: 0438 175 906 Emails: sales@gewservice.com.au; admin@gewservice.com.au; accounts@gewservice.com.au; parts@gewservice.com.au; office@gewservice.com.au, reception@gewservice.com.au
Look and feel

```html
<!DOCTYPE html>
<html lang="en">
<head>
<meta charset="utf-8">
<title>Gumtree Engine Works – Business Card</title>
<link href="https://fonts.googleapis.com/css2?family=Montserrat:wght@400;500;800&display=swap" rel="stylesheet">
<style>
  :root {
    --brand-red: #e8202a;
    --ink: #1a1a1a;
    --paper: #ffffff;
    --backdrop: #cfcfcf;
  }
  * { margin: 0; padding: 0; box-sizing: border-box; }
  html, body {
    width: 1200px; height: 984px; overflow: hidden;
    background: var(--backdrop);
    font-family: "Montserrat", Arial, sans-serif;
  }
  .card {
    position: absolute; left: 250px;
    width: 700px; height: 400px;
    box-shadow: 0 4px 14px rgba(0,0,0,.25);
    overflow: hidden;
  }
  .card-front {
    top: 52px; background: var(--brand-red);
    display: flex; align-items: center; justify-content: center; gap: 16px;
  }
  .front-mark {
    width: 34px; height: 34px; border-radius: 50%; background: var(--paper);
  }
  .front-name {
    color: var(--paper); font-weight: 800; font-size: 40px; letter-spacing: .5px;
  }
  .card-back { top: 512px; background: var(--paper); }
  .back-brand {
    position: absolute; left: 40px; top: 62px;
    display: flex; align-items: center; gap: 10px;
  }
  .back-mark { width: 22px; height: 22px; border-radius: 50%; background: var(--brand-red); }
  .back-name { color: var(--brand-red); font-weight: 800; font-size: 22px; }
  .owners {
    position: absolute; left: 30px; top: 150px; width: 320px; text-align: right;
  }
  .owners-names {
    color: var(--brand-red); font-weight: 800; font-size: 17px; text-transform: uppercase;
    line-height: 1.4;
  }
  .owners-role, .owners-abn { color: var(--ink); font-size: 17px; line-height: 1.5; }
  .contact-list {
    position: absolute; left: 378px; top: 22px; list-style: none;
  }
  .contact-item {
    display: flex; align-items: center; gap: 12px;
    height: 29px; font-size: 16.5px; color: var(--ink);
  }
  .contact-icon { width: 18px; height: 18px; flex: none; }
  .address-band {
    position: absolute; left: 0; top: 300px; width: 100%; height: 44px;
    background: var(--brand-red); color: var(--paper);
    font-size: 17px; display: flex; align-items: center; padding-left: 60px;
    white-space: nowrap;
  }
  .postal-line {
    position: absolute; left: 100px; top: 356px; font-size: 17px; color: var(--ink);
    white-space: nowrap;
  }
</style>
</head>
<body>
  <section class="card card-front">
    <span class="front-mark"></span>
    <span class="front-name">Gumtree Engine Works</span>
  </section>

  <section class="card card-back">
    <div class="back-brand">
      <span class="back-mark"></span>
      <span class="back-name">Gumtree Engine Works</span>
    </div>

    <div class="owners">
      <p class="owners-names">Doug &amp; Marisol Brent-Coyle</p>
      <p class="owners-role">Owners/Directors</p>
      <p class="owners-abn">ABN: 41 917 302 846</p>
    </div>

    <ul class="contact-list">
      <li class="contact-item">
        <svg class="contact-icon" viewBox="0 0 24 24"><path fill="#e8202a" d="M6.6 10.8a15 15 0 0 0 6.6 6.6l2.2-2.2c.3-.3.7-.4 1-.2 1.1.4 2.3.6 3.6.6.6 0 1 .4 1 1V20c0 .6-.4 1-1 1A17 17 0 0 1 3 4c0-.6.4-1 1-1h3.5c.6 0 1 .4 1 1 0 1.3.2 2.5.6 3.6.1.3 0 .7-.2 1z"/></svg>
        4712 9083</li>
      <li class="contact-item">
        <svg class="contact-icon" viewBox="0 0 24 24"><rect x="6" y="2" width="12" height="20" rx="2" fill="none" stroke="#e8202a" stroke-width="2"/><circle cx="12" cy="18" r="1.2" fill="#e8202a"/></svg>
        0438 175 906</li>
      <li class="contact-item"><svg class="contact-icon" viewBox="0 0 24 24"><rect x="2" y="5" width="20" height="14" fill="#e8202a"/><path d="M2 5l10 8 10-8" fill="none" stroke="#fff" stroke-width="1.6"/></svg>sales@gewservice.com.au</li>
      <li class="contact-item"><svg class="contact-icon" viewBox="0 0 24 24"><rect x="2" y="5" width="20" height="14" fill="#e8202a"/><path d="M2 5l10 8 10-8" fill="none" stroke="#fff" stroke-width="1.6"/></svg>admin@gewservice.com.au</li>
      <li class="contact-item"><svg class="contact-icon" viewBox="0 0 24 24"><rect x="2" y="5" width="20" height="14" fill="#e8202a"/><path d="M2 5l10 8 10-8" fill="none" stroke="#fff" stroke-width="1.6"/></svg>accounts@gewservice.com.au</li>
      <li class="contact-item"><svg class="contact-icon" viewBox="0 0 24 24"><rect x="2" y="5" width="20" height="14" fill="#e8202a"/><path d="M2 5l10 8 10-8" fill="none" stroke="#fff" stroke-width="1.6"/></svg>parts@gewservice.com.au</li>
      <li class="contact-item"><svg class="contact-icon" viewBox="0 0 24 24"><rect x="2" y="5" width="20" height="14" fill="#e8202a"/><path d="M2 5l10 8 10-8" fill="none" stroke="#fff" stroke-width="1.6"/></svg>office@gewservice.com.au</li>
      <li class="contact-item"><svg class="contact-icon" viewBox="0 0 24 24"><rect x="2" y="5" width="20" height="14" fill="#e8202a"/><path d="M2 5l10 8 10-8" fill="none" stroke="#fff" stroke-width="1.6"/></svg>reception@gewservice.com.au</li>
      <li class="contact-item">
        <svg class="contact-icon" viewBox="0 0 24 24"><circle cx="12" cy="12" r="10" fill="#e8202a"/><path d="M2 12h20M12 2c3 3 3 17 0 20M12 2c-3 3-3 17 0 20" fill="none" stroke="#fff" stroke-width="1.4"/></svg>
        www.gewservice.com.au</li>
    </ul>

    <div class="address-band">317 Wattlebrook Street BINDARRA CREEK QLD 4873 Postal</div>
    <p class="postal-line">PO Box 5791 BINDARRA CREEK QLD 4873</p>
  </section>
</body>
</html>
```